Custom Software Solutions

web design for a small custom programming company in Brisbane Australia. Specialize in business finance solutions, Tovix Desk automation and programming and data analysis. The design should portray professionalism and honesty. Main applications deal with financial accounting reporting and analysis. Would like to see colors blue and purple used (but sparsely). added file is company logo. Trading name is RN Ventures, while the official company name is RN Ventures (QLD) Pty Ltd.

Target Market(s)

current clients for support
marketing tool for prospective clients

Industry/Entity Type

Business

Number of Pages Required

5+ page

Font styles to use
Sans Serif

Colors
0555a3
a54599
ffffff

Requirements
Must have
• introduction
• blog for news and tips
• previous and current clients/projects page
• contact us page with email submission form
Should not have
• social media links

```html
<!DOCTYPE html>
<html lang="en">
<head>
<meta charset="utf-8">
<title>RN Ventures – Custom Software Solutions</title>
<link href="https://fonts.googleapis.com/css2?family=Open+Sans:wght@400;600;700;800&display=swap" rel="stylesheet">
<style>
  :root {
    --blue: #0555a3;
    --sky: #1a9ad6;
    --purple: #a54599;
    --ink: #2b2b2b;
    --muted: #6f6f6f;
    --light: #f3f3f3;
    --line: #dcdcdc;
    --footer: #2f2f31;
    --white: #ffffff;
  }
  * { box-sizing: border-box; margin: 0; padding: 0; }
  html, body { width: 855px; height: 1200px; overflow: hidden; background: var(--white); }
  body { font-family: "Open Sans", Arial, sans-serif; color: var(--ink); }
  .page { width: 855px; height: 1200px; position: relative; overflow: hidden; }

  /* Header */
  .site-header { height: 92px; display: flex; align-items: center; justify-content: space-between; padding: 0 42px 0 40px; }
  .brand { display: flex; align-items: center; gap: 10px; }
  .brand-mark { width: 30px; height: 30px; border-radius: 50%; background: var(--blue); }
  .brand-name { font-size: 24px; font-weight: 600; color: var(--blue); letter-spacing: .2px; }
  .main-nav { display: flex; gap: 26px; }
  .main-nav a { font-size: 11px; font-weight: 600; color: var(--ink); text-decoration: none; padding-bottom: 6px; }
  .main-nav a.active { color: var(--sky); border-bottom: 2px solid var(--sky); }

  /* Hero */
  .hero { position: relative; height: 330px; background: linear-gradient(160deg, #d9d9d9 0%, #a9a9ab 40%, #6b6b6e 75%, #4b4b4e 100%); color: var(--white); text-align: center; }
  .hero-title { padding-top: 78px; font-size: 56px; font-weight: 800; letter-spacing: 2px; }
  .hero-sub { margin: 10px auto 0; width: 420px; font-size: 10px; line-height: 1.5; }
  .btn { display: inline-block; margin-top: 22px; background: var(--sky); color: var(--white); font-size: 11px; font-weight: 600; padding: 10px 24px; border-radius: 3px; text-decoration: none; }
  .hero-dots { position: absolute; bottom: 20px; left: 0; right: 0; display: flex; justify-content: center; gap: 7px; }
  .hero-dots span { width: 7px; height: 7px; border-radius: 50%; background: rgba(255,255,255,.55); }
  .hero-dots span.on { background: var(--white); }

  /* Services */
  .services { display: flex; gap: 34px; padding: 36px 40px 0; height: 218px; }
  .service { flex: 1; }
  .service-head { display: flex; align-items: center; gap: 14px; }
  .service-icon { width: 48px; height: 48px; border-radius: 50%; background: var(--sky); display: flex; align-items: center; justify-content: center; flex: none; }
  .service-title { font-size: 14px; font-weight: 800; line-height: 1.2; text-transform: uppercase; }
  .service p { margin-top: 14px; font-size: 9.5px; line-height: 1.55; color: var(--muted); }
  .more { display: inline-flex; align-items: center; gap: 5px; margin-top: 12px; font-size: 9.5px; color: var(--sky); text-decoration: none; font-weight: 600; }

  /* Section bands */
  .band { position: relative; margin: 0 40px; height: 38px; background: var(--light); border-bottom: 2px solid var(--sky); display: flex; align-items: center; padding-left: 62px; }
  .band-icon { position: absolute; left: 2px; top: -5px; width: 44px; height: 44px; border-radius: 50%; background: var(--white); border: 3px solid var(--sky); display: flex; align-items: center; justify-content: center; }
  .band-title { font-size: 12px; font-weight: 800; text-transform: uppercase; }
  .band-arrows { position: absolute; right: 8px; display: flex; gap: 4px; }
  .band-arrows span { width: 18px; height: 18px; background: var(--white); border: 1px solid var(--line); display: flex; align-items: center; justify-content: center; }

  /* Testimonials */
  .testimonials { display: flex; gap: 40px; padding: 34px 64px 0; height: 190px; }
  .quote { flex: 1; position: relative; padding-left: 40px; }
  .quote-mark { position: absolute; left: 0; top: -6px; font-size: 46px; font-weight: 800; color: #cfcfcf; line-height: 1; }
  .quote p { font-size: 9.5px; line-height: 1.6; color: var(--muted); }
  .quote cite { display: block; margin-top: 28px; font-size: 9.5px; font-style: italic; color: var(--ink); }

  /* Latest posts */
  .posts { display: flex; gap: 32px; padding: 26px 40px 0; height: 210px; }
  .post { flex: 1; display: flex; gap: 18px; }
  .post-photo { width: 150px; height: 118px; flex: none; }
  .photo-team { background: linear-gradient(135deg, #cfd8e2, #7c8796 60%, #3e4552); }
  .photo-work { background: linear-gradient(135deg, #e4e6ea, #9aa1ab 55%, #4a505a); }
  .post-title { font-size: 12px; font-weight: 800; text-transform: uppercase; }
  .post-meta { margin-top: 4px; font-size: 9px; color: var(--muted); }
  .post p { margin-top: 10px; font-size: 9.5px; line-height: 1.55; color: var(--muted); }

  /* Footer */
  .site-footer { position: absolute; bottom: 0; left: 0; right: 0; height: 84px; background: var(--footer); color: #cfcfcf; text-align: center; padding-top: 26px; }
  .footer-nav { display: flex; justify-content: center; gap: 28px; }
  .footer-nav a { font-size: 10px; color: #e6e6e6; text-decoration: none; }
  .copyright { margin-top: 12px; font-size: 9px; }
</style>
</head>
<body>
<div class="page">

  <header class="site-header">
    <div class="brand">
      <span class="brand-mark"></span>
      <span class="brand-name">RN Ventures</span>
    </div>
    <nav class="main-nav">
      <a href="#" class="active">HOME</a>
      <a href="#">ABOUT US</a>
      <a href="#">SERVICE</a>
      <a href="#">BLOG</a>
      <a href="#">CLIENTS</a>
      <a href="#">CONTACT US</a>
    </nav>
  </header>

  <section class="hero" role="img" aria-label="Photograph of a laptop on an office desk behind the headline">
    <h1 class="hero-title">WEB SOLUTIONS</h1>
    <p class="hero-sub">Reliable custom software for finance, reporting and analysis built for growing businesses across Queensland.</p>
    <a href="#" class="btn">Read More</a>
    <div class="hero-dots"><span></span><span class="on"></span><span></span></div>
  </section>

  <section class="services">
    <article class="service">
      <div class="service-head">
        <span class="service-icon">
          <svg width="24" height="24" viewBox="0 0 24 24" fill="none" stroke="#fff" stroke-width="2"><rect x="3" y="7" width="18" height="13" rx="2"/><path d="M9 7V4h6v3M3 12h18"/></svg>
        </span>
        <h2 class="service-title">Business Finance<br>Solutions</h2>
      </div>
      <p>Sed ut perspiciatis unde omnis iste natus error sit voluptatem accusantium doloremque laudantium, totam rem aperiam.</p>
      <a href="#" class="more">Read More <svg width="12" height="8" viewBox="0 0 12 8"><rect width="8" height="8" fill="#1a9ad6"/><path d="M8 4l4-3v6z" fill="#1a9ad6"/></svg></a>
    </article>
    <article class="service">
      <div class="service-head">
        <span class="service-icon">
          <svg width="24" height="24" viewBox="0 0 24 24" fill="none" stroke="#fff" stroke-width="2"><rect x="3" y="4" width="18" height="12" rx="1"/><path d="M8 20h8M12 16v4"/></svg>
        </span>
        <h2 class="service-title">Tovix Desk Automation<br>and Programming</h2>
      </div>
      <p>Sed ut perspiciatis unde omnis iste natus error sit voluptatem accusantium doloremque laudantium, totam rem aperiam.</p>
      <a href="#" class="more">Read More <svg width="12" height="8" viewBox="0 0 12 8"><rect width="8" height="8" fill="#1a9ad6"/><path d="M8 4l4-3v6z" fill="#1a9ad6"/></svg></a>
    </article>
    <article class="service">
      <div class="service-head">
        <span class="service-icon">
          <svg width="24" height="24" viewBox="0 0 24 24" fill="none" stroke="#fff" stroke-width="2"><circle cx="12" cy="12" r="3.5"/><path d="M12 2v4M12 18v4M2 12h4M18 12h4M5 5l3 3M16 16l3 3M5 19l3-3M16 8l3-3"/></svg>
        </span>
        <h2 class="service-title">Data Analysis</h2>
      </div>
      <p>Sed ut perspiciatis unde omnis iste natus error sit voluptatem accusantium doloremque laudantium, totam rem aperiam.</p>
      <a href="#" class="more">Read More <svg width="12" height="8" viewBox="0 0 12 8"><rect width="8" height="8" fill="#1a9ad6"/><path d="M8 4l4-3v6z" fill="#1a9ad6"/></svg></a>
    </article>
  </section>

  <div class="band">
    <span class="band-icon">
      <svg width="18" height="18" viewBox="0 0 24 24" fill="#1a9ad6"><path d="M3 4h18v12H9l-5 4v-4H3z"/></svg>
    </span>
    <h2 class="band-title">Testimonials</h2>
    <div class="band-arrows">
      <span><svg width="6" height="8" viewBox="0 0 6 8"><path d="M5 0L0 4l5 4z" fill="#999"/></svg></span>
      <span><svg width="6" height="8" viewBox="0 0 6 8"><path d="M1 0l5 4-5 4z" fill="#999"/></svg></span>
    </div>
  </div>

  <section class="testimonials">
    <blockquote class="quote">
      <span class="quote-mark">&ldquo;</span>
      <p>Sed ut perspiciatis unde omnis iste natus error sit voluptatem accusantium doloremque laudantium, totam rem aperiam, eaque ipsa quae ab illo.</p>
      <cite>_ Liam Carter</cite>
    </blockquote>
    <blockquote class="quote">
      <span class="quote-mark">&ldquo;</span>
      <p>Nemo enim ipsam voluptatem quia voluptas sit aspernatur aut odit aut fugit, sed quia consequuntur magni dolores eos qui ratione.</p>
      <cite>_ Nora</cite>
    </blockquote>
  </section>

  <div class="band">
    <span class="band-icon">
      <svg width="16" height="18" viewBox="0 0 20 24" fill="none" stroke="#1a9ad6" stroke-width="2.5"><path d="M2 2h11l5 5v15H2z"/><path d="M6 11h8M6 16h8"/></svg>
    </span>
    <h2 class="band-title">Latest Post</h2>
    <div class="band-arrows">
      <span><svg width="6" height="8" viewBox="0 0 6 8"><path d="M5 0L0 4l5 4z" fill="#999"/></svg></span>
      <span><svg width="6" height="8" viewBox="0 0 6 8"><path d="M1 0l5 4-5 4z" fill="#999"/></svg></span>
    </div>
  </div>

  <section class="posts">
    <article class="post">
      <div class="post-photo photo-team" role="img" aria-label="Photograph of a business team standing together"></div>
      <div>
        <h3 class="post-title">Post With Heading</h3>
        <div class="post-meta">Posted by: 15 Sep 2014</div>
        <p>If your computer or network is protected by a firewall or proxy, make sure it is permitted to access the Web. Check the address for typing errors such as www.sample.test.</p>
      </div>
    </article>
    <article class="post">
      <div class="post-photo photo-work" role="img" aria-label="Photograph of a businessman working at a desk"></div>
      <div>
        <h3 class="post-title">Post2</h3>
        <div class="post-meta">Posted by: 15 Sep 2014</div>
        <p>If your computer or network is protected by a firewall or proxy, make sure it is permitted to access the Web.</p>
      </div>
    </article>
  </section>

  <footer class="site-footer">
    <nav class="footer-nav">
      <a href="#">HOME</a>
      <a href="#">ABOUT US</a>
      <a href="#">SERVICE</a>
      <a href="#">BLOG</a>
      <a href="#">CLIENTS</a>
      <a href="#">CONTACT US</a>
    </nav>
    <p class="copyright">Copyright @2014 RN Ventures All Right Reserved</p>
  </footer>

</div>
</body>
</html>
```